Brett Olsen Building Business Card Design

Hi,

I need a business card for my Building company.
I am a Builder and build homes for clients.
I am looking for a sophisticated logo that can be used on business cards, envelopes and letter heads.
I am trying to take my business to the next level and need a professional business card.

Colours: Please use white, black, dark grey and bright blue.

Thank you,

Carol and Brett.

Target Market(s)

1. Home and Building Companies 2. Potential customers

Industry/Entity Type

Business

Contact Information for Business Card

Brett Olsen Building PTY LTD

Brett Olsen

Director

A.B.N. 37 829 516 073

BUILDERS LICENCE No. 573019k

Mobile: 0412 907 381

Email: brettolsenbuilding@mailvane.com.au

Requirements
Must have
• The following is compulsory to have in the designs:

Brett Olsen Building PTY LTD (business name)

Brett Olsen (contact name)

Director (position)

A.B.N. 37 829 516 073

Builders Licence No. 573019k

Mobile: 0412 907 381

Nice to have
• Logo for business
Should not have
• Should not be cluttered.

I am looking for a clean, sophisticated and professional business card design.

```html
<!DOCTYPE html>
<html lang="en">
<head>
<meta charset="utf-8">
<title>Brett Olsen Building – Business Card</title>
<link rel="stylesheet" href="https://fonts.googleapis.com/css2?family=Jost:wght@300;400&display=swap">
<style>
  :root {
    --card-blue: #00ffff;
    --ink-white: #ffffff;
    --ink-black: #111111;
  }
  html, body {
    margin: 0;
    padding: 0;
    width: 1200px;
    height: 741px;
    overflow: hidden;
    background: var(--card-blue);
  }
  .card {
    position: relative;
    width: 1200px;
    height: 741px;
    background: var(--card-blue);
    font-family: "Jost", "Futura", sans-serif;
    font-weight: 300;
  }
  .card p { margin: 0; position: absolute; left: 268px; white-space: nowrap; }

  .brand-name {
    top: 168px;
    font-size: 66px;
    font-weight: 300;
    color: var(--ink-white);
    letter-spacing: 0.5px;
  }

  .credentials { color: var(--ink-white); font-size: 37px; }
  .credentials .label { font-weight: 400; }
  .abn { top: 300px; }
  .licence { top: 351px; }

  .contact-name {
    top: 443px;
    font-size: 41px;
    font-weight: 400;
    color: var(--ink-black);
  }
  .contact-role {
    top: 488px;
    font-size: 41px;
    color: var(--ink-black);
  }
  .phone {
    top: 562px;
    font-size: 39px;
    color: var(--ink-black);
    letter-spacing: 1px;
  }
  .email {
    top: 612px;
    font-size: 36px;
    color: var(--ink-black);
  }
</style>
</head>
<body>
  <main class="card">
    <p class="brand-name">Brett Olsen Building PTY LTD</p>

    <p class="credentials abn"><span class="label">A.B.N</span> 37 829 516 073</p>
    <p class="credentials licence"><span class="label">BUILDERS LICENCE</span> No.573019k</p>

    <p class="contact-name">Brett Olsen</p>
    <p class="contact-role">Director</p>

    <p class="phone">0412 907 381</p>
    <p class="email">brettolsenbuilding@mailvane.com.au</p>
  </main>
</body>
</html>
```